Brambury Logistics

Create a modern, simple, Elegant business card design for my business.

Services: Tamo Trucks, Transport, Contract Logistics,

Industry/Entity Type

Business

Contact Information for Business Card

Include all details same as old card plus new website address: www.bramburylogistics.com.au

Requirements
Must have
• Similar colors to Logo.

```html
<!DOCTYPE html>
<html lang="en">
<head>
<meta charset="utf-8">
<title>Brambury Logistics — Business Card</title>
<link href="https://fonts.googleapis.com/css2?family=Lato:wght@400;700;900&display=swap" rel="stylesheet">
<style>
  :root {
    --backdrop: #3b3b3c;
    --brand-blue: #0b6aa2;
    --brand-blue-deep: #17507f;
    --brand-blue-text: #2d679c;
    --steel-grey: #6e6f72;
    --stripe-grey: #8a8b8e;
    --paper: #ffffff;
  }
  * { margin: 0; padding: 0; box-sizing: border-box; }
  html, body {
    width: 1200px; height: 810px; overflow: hidden;
    background: var(--backdrop);
    font-family: 'Lato', sans-serif;
  }
  .canvas { position: relative; width: 1200px; height: 810px; }

  .card {
    position: absolute;
    width: 520px; height: 298px;
    box-shadow: 0 10px 24px rgba(0,0,0,0.35);
    overflow: hidden;
  }

  /* Front: brand side */
  .card--front {
    left: 70px; top: 100px;
    background: linear-gradient(180deg, var(--brand-blue-deep) 0%, var(--brand-blue) 100%);
    color: var(--paper);
    text-align: center;
  }
  .front__brand {
    position: absolute; left: 0; right: 0; top: 96px;
    font-size: 38px; font-weight: 900; letter-spacing: 0.5px;
  }
  .front__services {
    position: absolute; left: 0; right: 0; top: 196px;
    font-size: 13px; line-height: 20px; font-weight: 400;
  }

  /* Back: contact side */
  .card--back {
    left: 610px; top: 410px;
    background: var(--paper);
  }
  .back__wave { position: absolute; inset: 0; }
  .back__brand {
    position: absolute; left: 34px; top: 58px;
    font-size: 32px; font-weight: 900;
    color: var(--steel-grey);
  }
  .back__person { position: absolute; left: 40px; top: 150px; }
  .person__name { font-size: 20px; font-weight: 400; color: var(--brand-blue-text); }
  .person__title { font-size: 13px; color: var(--steel-grey); margin-top: 4px; }

  .back__contacts {
    position: absolute; right: 22px; bottom: 28px;
    list-style: none; text-align: right;
    color: var(--paper); font-size: 12.5px;
  }
  .back__contacts li {
    display: flex; justify-content: flex-end; align-items: center;
    gap: 8px; line-height: 21px;
  }
  .contact__icon { width: 12px; height: 12px; fill: var(--paper); flex: none; }
</style>
</head>
<body>
<main class="canvas">

  <section class="card card--front" aria-label="Business card front">
    <div class="front__brand">Brambury Logistics</div>
    <p class="front__services">Services:<br>Tamo Trucks, Transport, Contract Logistics</p>
  </section>

  <section class="card card--back" aria-label="Business card back">
    <svg class="back__wave" viewBox="0 0 520 298" preserveAspectRatio="none" aria-hidden="true">
      <path d="M0,240 C190,245 370,170 445,0 L520,0 L520,298 L0,298 Z" fill="var(--stripe-grey)"/>
      <path d="M0,254 C200,258 385,180 460,0 L520,0 L520,298 L0,298 Z" fill="var(--brand-blue)"/>
    </svg>

    <div class="back__brand">Brambury Logistics</div>

    <div class="back__person">
      <div class="person__name">Daniel Harker</div>
      <div class="person__title">President</div>
    </div>

    <ul class="back__contacts">
      <li>0412305768
        <svg class="contact__icon" viewBox="0 0 24 24" aria-hidden="true"><path d="M6.6 10.8a15 15 0 0 0 6.6 6.6l2.2-2.2c.3-.3.7-.4 1-.2 1.1.4 2.3.6 3.6.6.6 0 1 .4 1 1V20c0 .6-.4 1-1 1A17 17 0 0 1 3 4c0-.6.4-1 1-1h3.5c.6 0 1 .4 1 1 0 1.3.2 2.5.6 3.6.1.3 0 .7-.2 1z"/></svg>
      </li>
      <li>office@bramburylogistics.com.au
        <svg class="contact__icon" viewBox="0 0 24 24" aria-hidden="true"><path d="M2 5h20v14H2z M3.5 6.5 12 13l8.5-6.5" fill="none" stroke="#fff" stroke-width="2"/></svg>
      </li>
      <li>www.bramburylogistics.com.au
        <svg class="contact__icon" viewBox="0 0 24 24" aria-hidden="true"><g fill="none" stroke="#fff" stroke-width="2"><circle cx="12" cy="12" r="9.5"/><ellipse cx="12" cy="12" rx="4" ry="9.5"/><path d="M2.5 12h19"/></g></svg>
      </li>
    </ul>
  </section>

</main>
</body>
</html>
```